Croatia Luxury Cruise Brochure

1) Front page instead of By Traveling with Lirel please put by Gable Roaming Venture – same on the last page where you have her contacts
2) Can you please add into the second page where you have ‘Welcome to your Croatia trip’ itinerary at glance. You can put it just below the text you have. Create a nice looking table .
D1 August 05, 2023 Arrival to Dubrovnik , Welcome cocktail party on Dubrovnik city walls
D2 August 06, 2023 Dubrovnik Highlights city tour – Embark sail to Elafiti
D3 August 07, 2023 Sail to Mljet island and day at leisure at sea
D4 August 08, 2023 Peljesac Wine Tasting with Live Music – Sail to Korcula
D5 August 09, 2023 Korcula Highlights Explorer Tour & Local Estate Dinner
D6 August 10, 2023 Korcula to Vis Island sail
D7 August 11, 2023 Vis Militarty Tour -sail to Pakleni Islands Veskaro sunset cocktails
D8 August 12, 2023 Hvar island – sail to Split
D9 August 13, 2023 Disembark – Split & Trogir UNESCO tours with 6-course wine dinner
D10 August 14, 2023 Fly out
Note: All tours & Experiences are optional add ons except the Cocktail reception on Dubrovnik city walls
3) Changes to the itinerary:
D1 is now arrival to Dubrovnik day earlier (AUGU5) and the rest is all moved accordingly. Please check the link
https://portal.trevolanto. example/itinerary/custom-trip-prepared-for-lirel-group/
4) Inclusion/Exclusion page we need to update a little. Please make 3 different categories with a note for booking conditions.
Inclusions
• All transfers per itinerary including airport pick up and drop off
• 7 nights cruise on MS Halcyra on half board basis
• All meals stated per itinerary
• Captains dinner
• Unlimited water
• Masseuse on board
• Service of 11 crew members
• Cruise director
• Unlimited WiFi
• Daily cleaning
• Arrival refreshments
• Premium docking
• Usage of non motorized water toys
• Exclusive cocktail reception on Dubrovnik city walls with live music and snacks
Optional Tours
• Dubrovnik Highlights Explorer tour
• Peljesac Wine tour with live music
• Korcula explorer tour with local estate dinner
• Vis Military tour
• Veskaro Lounge bar reservation (min spend EUR100 per person)
• Split & Trogir UNESCO Explorer tour
• 6-course farewell dinner with local wine pairing
• 1 night post stay in Bellavi 5* hotel in Split (This is added on optional)
Extras
• Tips for the crew
• Beverage consumption
• Usage of motorized water toys – EUR150 per hour
• International flights
• Any personal expenses
Booking conditions
30 % non-refundable deposit needed upon confirmation
Balance of the trip and any optional tours picked are due 06 May, 2023
Target Market(s)
Luxury travelers from USA and Canada
Industry/Entity Type
Tourism

```html
<!DOCTYPE html>
<html lang="en">
<head>
<meta charset="utf-8">
<title>Croatia – Luxury Explorer Cruise Brochure</title>
<link rel="stylesheet" href="https://fonts.googleapis.com/css2?family=Lato:wght@300;400;700&family=Fira+Sans:wght@300;400&display=swap">
<style>
  :root {
    --brand-red: #e63c22;
    --paper: #ffffff;
    --ink: #1a1a1a;
    --label: #333333;
    --rule: #c9a77a;
    --row-line: #e6d9c6;
    --fold: #b5b5b5;
    --shadow: rgba(0,0,0,0.18);
  }
  * { margin: 0; padding: 0; box-sizing: border-box; }
  html, body { width: 1200px; height: 2741px; overflow: hidden; background: var(--paper); }
  .canvas { position: relative; width: 1200px; height: 2741px; font-family: "Lato", sans-serif; color: var(--ink); }
  .abs { position: absolute; }
  .photo { position: absolute; }

  /* Front cover */
  .cover-band { left: 0; top: 195px; width: 1200px; height: 244px; background: var(--brand-red); }
  .cover-title { left: 27px; top: 226px; font-weight: 300; font-size: 118px; letter-spacing: 14px; color: #fff; line-height: 1; }
  .cover-credit { left: 32px; top: 372px; font-weight: 400; font-size: 15px; letter-spacing: 2px; color: #fff; }
  .cover-subtitle { left: 589px; top: 364px; font-weight: 400; font-size: 19px; color: #fff; letter-spacing: 0.2px; }
  .cover-dates { left: 589px; top: 394px; font-weight: 700; font-size: 14px; line-height: 14px; letter-spacing: 1px; color: #fff; }
  .cover-mosaic { left: 0; top: 439px; width: 1200px; height: 440px; background: var(--brand-red); }

  .spread-label { font-family: "Fira Sans", sans-serif; font-weight: 300; font-size: 19px; color: var(--label); transform: translateX(-50%); white-space: nowrap; }

  /* Spreads */
  .spread { left: 0; width: 1197px; background: var(--paper); box-shadow: 0 2px 6px var(--shadow); }
  .fold { left: 600px; width: 0; border-left: 2px dashed var(--fold); }
  .side-tab { left: 0; width: 23px; background: var(--brand-red); }
  .section-title { font-family: "Fira Sans", sans-serif; font-weight: 300; color: var(--ink); line-height: 1; }
  .title-rule { height: 1px; background: var(--rule); }
  .body-copy { font-size: 6px; line-height: 8.4px; color: var(--ink); text-align: justify; }
  .body-copy p + p { margin-top: 6px; }
  .page-number { left: 1126px; font-size: 7px; }

  /* Itinerary at a glance */
  .glance-title { left: 620px; top: 100px; font-family: "Fira Sans", sans-serif; font-weight: 300; font-size: 18px; line-height: 1; }
  .glance-table { left: 620px; top: 126px; width: 270px; border-collapse: collapse; font-size: 7.5px; line-height: 9px; }
  .glance-table th { background: var(--brand-red); color: #fff; font-weight: 700; text-align: left; padding: 4px 4px; letter-spacing: 0.5px; }
  .glance-table td { padding: 3px 4px; border-bottom: 1px solid var(--row-line); vertical-align: top; height: 24px; }
  .glance-table .col-day { width: 26px; font-weight: 700; color: var(--brand-red); }
  .glance-table .col-date { width: 70px; white-space: nowrap; }
  .glance-note { left: 620px; top: 402px; width: 270px; font-size: 6.5px; line-height: 8.5px; font-style: italic; }

  /* Back page */
  .back-band { left: 0; top: 2304px; width: 1200px; height: 437px; background: var(--brand-red); color: #fff; }
  .terms-col { top: 26px; width: 340px; }
  .terms-heading { font-family: "Fira Sans", sans-serif; font-weight: 300; font-size: 22px; line-height: 1; margin-bottom: 10px; }
  .terms-list { list-style: none; font-size: 10px; line-height: 13.5px; }
  .terms-list li { position: relative; padding-left: 11px; }
  .terms-list li::before { content: ""; position: absolute; left: 0; top: 5px; width: 4px; height: 4px; background: #fff; border-radius: 50%; }
  .terms-block { margin-top: 18px; }
  .terms-note { font-size: 10px; line-height: 13.5px; }
  .back-credit { left: 60px; top: 298px; }
  .back-credit-name { font-size: 16px; font-weight: 400; letter-spacing: 1.5px; }
  .back-credit-link { font-size: 10px; margin-top: 4px; }
</style>
</head>
<body>
<main class="canvas">

  <!-- Front cover -->
  <section class="front-cover">
    <div class="photo" role="img" aria-label="Wooden boardwalk over a clear stream in autumn forest"
         style="left:0;top:0;width:1200px;height:195px;background:linear-gradient(90deg,#3b6e9a 0%,#a07a4e 25%,#8a6a3e 40%,#3f6b2a 60%,#6e5a22 80%,#3c5e22 100%);"></div>
    <div class="abs cover-band"></div>
    <h1 class="abs cover-title">CROATIA</h1>
    <p class="abs cover-credit">BY GABLE ROAMING VENTURE</p>
    <p class="abs cover-subtitle">LUXURY EXPLORER CRUISE ON HALCYRA MINI CRUISER</p>
    <p class="abs cover-dates">05 AUGUST - 14 AUGUST, 2023</p>

    <div class="abs cover-mosaic"></div>
    <div class="photo" role="img" aria-label="Cascading waterfalls surrounded by green forest"
         style="left:0;top:439px;width:450px;height:440px;background:linear-gradient(180deg,#8fb5d8 0%,#3f6f3a 30%,#cfe3ef 55%,#1f78b4 80%,#124a6a 100%);"></div>
    <div class="photo" role="img" aria-label="Hilltop town seen through a stone window"
         style="left:455px;top:439px;width:285px;height:191px;background:linear-gradient(180deg,#7a6a50 0%,#4a6fc0 30%,#6f8f4a 65%,#8a7a5a 100%);"></div>
    <div class="photo" role="img" aria-label="Waterfront promenade with bell tower at sunset"
         style="left:745px;top:439px;width:455px;height:191px;background:linear-gradient(180deg,#e8b070 0%,#c7a070 40%,#6f8aa0 65%,#3f6a8a 100%);"></div>
    <div class="photo" role="img" aria-label="Small island with monastery in a green lake"
         style="left:455px;top:635px;width:186px;height:189px;background:linear-gradient(180deg,#3f7a2f 0%,#5a9a40 40%,#2f6a3a 65%,#4a9a8a 100%);"></div>
    <div class="photo" role="img" aria-label="Colourful stained glass window"
         style="left:646px;top:635px;width:186px;height:189px;background:linear-gradient(135deg,#3a7ac0 0%,#b44a8a 35%,#e8c070 60%,#2f8ab0 100%);"></div>
    <div class="photo" role="img" aria-label="Old stone fortress by the sea at dusk"
         style="left:837px;top:635px;width:363px;height:189px;background:linear-gradient(180deg,#e07050 0%,#b8a0a0 45%,#8a8090 70%,#6a6a8a 100%);"></div>
  </section>
  <p class="abs spread-label" style="left:685px;top:883px;">Front</p>

  <!-- About spread -->
  <section class="abs spread" style="top:923px;height:431px;">
    <div class="abs fold" style="top:0;height:431px;"></div>
    <span class="abs page-number" style="top:39px;">7</span>

    <div class="photo" role="img" aria-label="Carved stone architectural detail" style="left:66px;top:88px;width:103px;height:71px;background:linear-gradient(135deg,#8a7a6a,#c8b8a0,#6a5a4a);"></div>
    <div class="photo" role="img" aria-label="Mossy rocks and small waterfalls" style="left:177px;top:88px;width:104px;height:71px;background:linear-gradient(180deg,#2f4a2a,#5a7a3a,#4a6a5a);"></div>
    <div class="photo" role="img" aria-label="Bay with islets seen from above" style="left:288px;top:88px;width:103px;height:71px;background:linear-gradient(180deg,#7a9ab0,#4a6a8a,#2f4a5a);"></div>
    <div class="photo" role="img" aria-label="Rocky coastline with pine trees" style="left:66px;top:165px;width:103px;height:72px;background:linear-gradient(180deg,#8ab0d8,#3a6a3a,#2f5a8a);"></div>
    <div class="photo" role="img" aria-label="Waterfall pools in a national park" style="left:177px;top:165px;width:104px;height:72px;background:linear-gradient(180deg,#4a7a3a,#a0b0a0,#3a7a8a);"></div>
    <div class="photo" role="img" aria-label="Old town street with stone houses" style="left:288px;top:165px;width:103px;height:72px;background:linear-gradient(180deg,#7aa0c8,#c8a880,#8a6a4a);"></div>

    <div class="abs side-tab" style="top:258px;height:72px;"></div>
    <h2 class="abs section-title" style="left:66px;top:254px;font-size:40px;">ABOUT CROATIA</h2>
    <div class="abs title-rule" style="left:66px;top:308px;width:84px;"></div>
    <div class="abs body-copy" style="left:66px;top:330px;width:326px;">
      <p>The Croatian Coast is the premiere setting for the ultimate island hopping experience<br>The Dalmatian Islands in Croatia are among the most famous in the Mediterranean region. Wild, rugged, and hiding a thousand-year history, many are protected as national park and offer a varied and diverse cruising ground for an yacht charter. The cruising is splendid, encompassing long and short passages to charming anchorages amid rocky islets, ancient villages steeped in history, and translucent waters.<br>In total Croatia has over 1200 islands and islets to explore and visit so depending on your travel preference and travel style the combinations of itineraries are endless. Enjoy your cruise on mini cruiser MS Halcyra by visiting highlights of Adriatic coastline.</p>
    </div>

    <div class="photo" role="img" aria-label="Aerial view of green islands in a deep blue sea"
         style="left:455px;top:88px;width:742px;height:343px;background:linear-gradient(180deg,#a8c0d0 0%,#3f7aa8 15%,#1f5f8f 45%,#1a5a88 75%,#2f6a5a 100%);"></div>
  </section>
  <p class="abs spread-label" style="left:580px;top:1358px;">Internal pages</p>

  <!-- Itinerary spread -->
  <section class="abs spread" style="top:1386px;height:430px;">
    <div class="abs fold" style="top:0;height:86px;"></div>
    <div class="abs side-tab" style="top:87px;height:70px;"></div>
    <h2 class="abs section-title" style="left:62px;top:84px;font-size:42px;">05 August - 14 August, 2023</h2>
    <div class="abs body-copy" style="left:263px;top:141px;width:297px;">
      <p>Your journey begins on the sunlit walls of Dubrovnik, where a welcome cocktail sets the tone for ten days of island hopping, quiet anchorages and slow evenings on deck along the Dalmatian coast.</p>
      <p>Each day brings a new harbour: the green shores of Mljet, the vineyards of Peljesac, the old streets of Korcula and the hidden coves of Vis. Our small crew looks after every detail on board, from morning coffee to sunset cocktails, so you are free to swim, explore and rest at your own pace before the final evening in Split.</p>
    </div>

    <div class="photo" role="img" aria-label="Cabin with twin beds and portholes" style="left:0;top:253px;width:261px;height:177px;background:linear-gradient(180deg,#9a9a9a,#c8c0b0,#6a6a6a);"></div>
    <div class="photo" role="img" aria-label="Champagne bucket by a window with sea view" style="left:264px;top:253px;width:126px;height:90px;background:linear-gradient(180deg,#d8e0e8,#8a9aa8,#b0a890);"></div>
    <div class="photo" role="img" aria-label="Double bed cabin with decorative wall" style="left:264px;top:348px;width:126px;height:82px;background:linear-gradient(180deg,#8a7a6a,#c8b8a8,#e0d8d0);"></div>
    <div class="photo" role="img" aria-label="Aerial view of the mini cruiser on turquoise sea" style="left:395px;top:253px;width:165px;height:177px;background:linear-gradient(135deg,#1f7a7a,#3a9a9a,#e8e0d8 60%,#1f6a6a);"></div>

    <h3 class="abs glance-title">Itinerary at a glance</h3>
    <table class="abs glance-table">
      <thead>
        <tr><th>DAY</th><th>DATE</th><th>PROGRAM</th></tr>
      </thead>
      <tbody>
        <tr><td class="col-day">D1</td><td class="col-date">August 05, 2023</td><td>Arrival to Dubrovnik, Welcome cocktail party on Dubrovnik city walls</td></tr>
        <tr><td class="col-day">D2</td><td class="col-date">August 06, 2023</td><td>Dubrovnik Highlights city tour – Embark, sail to Elafiti</td></tr>
        <tr><td class="col-day">D3</td><td class="col-date">August 07, 2023</td><td>Sail to Mljet island and day at leisure at sea</td></tr>
        <tr><td class="col-day">D4</td><td class="col-date">August 08, 2023</td><td>Peljesac Wine Tasting with Live Music – Sail to Korcula</td></tr>
        <tr><td class="col-day">D5</td><td class="col-date">August 09, 2023</td><td>Korcula Highlights Explorer Tour &amp; Local Estate Dinner</td></tr>
        <tr><td class="col-day">D6</td><td class="col-date">August 10, 2023</td><td>Korcula to Vis Island sail</td></tr>
        <tr><td class="col-day">D7</td><td class="col-date">August 11, 2023</td><td>Vis Military Tour – sail to Pakleni Islands, Veskaro sunset cocktails</td></tr>
        <tr><td class="col-day">D8</td><td class="col-date">August 12, 2023</td><td>Hvar island – sail to Split</td></tr>
        <tr><td class="col-day">D9</td><td class="col-date">August 13, 2023</td><td>Disembark – Split &amp; Trogir UNESCO tours with 6-course wine dinner</td></tr>
        <tr><td class="col-day">D10</td><td class="col-date">August 14, 2023</td><td>Fly out</td></tr>
      </tbody>
    </table>
    <p class="abs glance-note">Note: All tours &amp; experiences are optional add ons except the Cocktail reception on Dubrovnik city walls.</p>

    <div class="photo" role="img" aria-label="Guest relaxing on a cabin balcony with sea view" style="left:905px;top:86px;width:292px;height:344px;background:linear-gradient(90deg,#2a2a2a 0%,#5a5a60 35%,#8a90a0 60%,#5a6a80 100%);"></div>
  </section>

  <!-- Back page -->
  <section class="back-page">
    <div class="photo" role="img" aria-label="Forest stream rushing over mossy rocks"
         style="left:0;top:1865px;width:1200px;height:439px;background:linear-gradient(180deg,#3f6a2a 0%,#5a8a3a 30%,#2f5a8a 60%,#6a9ac8 80%,#3a5a2a 100%);"></div>
    <div class="abs back-band">
      <div class="abs terms-col" style="left:60px;">
        <h3 class="terms-heading">Inclusions</h3>
        <ul class="terms-list">
          <li>All transfers per itinerary including airport pick up and drop off</li>
          <li>7 nights cruise on MS Halcyra on half board basis</li>
          <li>All meals stated per itinerary</li>
          <li>Captains dinner</li>
          <li>Unlimited water</li>
          <li>Masseuse on board</li>
          <li>Service of 11 crew members</li>
          <li>Cruise director</li>
          <li>Unlimited WiFi</li>
          <li>Daily cleaning</li>
          <li>Arrival refreshments</li>
          <li>Premium docking</li>
          <li>Usage of non motorized water toys</li>
          <li>Exclusive cocktail reception on Dubrovnik city walls with live music and snacks</li>
        </ul>
      </div>
      <div class="abs terms-col" style="left:440px;">
        <h3 class="terms-heading">Optional Tours</h3>
        <ul class="terms-list">
          <li>Dubrovnik Highlights Explorer tour</li>
          <li>Peljesac Wine tour with live music</li>
          <li>Korcula explorer tour with local estate dinner</li>
          <li>Vis Military tour</li>
          <li>Veskaro Lounge bar reservation (min spend EUR100 per person)</li>
          <li>Split &amp; Trogir UNESCO Explorer tour</li>
          <li>6-course farewell dinner with local wine pairing</li>
          <li>1 night post stay in Bellavi 5* hotel in Split (added on optional)</li>
        </ul>
      </div>
      <div class="abs terms-col" style="left:820px;">
        <h3 class="terms-heading">Extras</h3>
        <ul class="terms-list">
          <li>Tips for the crew</li>
          <li>Beverage consumption</li>
          <li>Usage of motorized water toys – EUR150 per hour</li>
          <li>International flights</li>
          <li>Any personal expenses</li>
        </ul>
        <div class="terms-block">
          <h3 class="terms-heading">Booking conditions</h3>
          <p class="terms-note">30% non-refundable deposit needed upon confirmation.<br>Balance of the trip and any optional tours picked are due 06 May, 2023.</p>
        </div>
      </div>
      <div class="abs back-credit">
        <p class="back-credit-name">GABLE ROAMING VENTURE</p>
        <p class="back-credit-link">https://portal.trevolanto. example/itinerary/custom-trip-prepared-for-lirel-group/</p>
      </div>
    </div>
    <p class="abs spread-label" style="left:704px;top:2658px;">BackPage</p>
  </section>

</main>
</body>
</html>
```